Déménagement Résidentiel & Commerciale

Déménagement Vellour

Depuis des années, Déménagement Vellour déplace ses clients dans et autour de la grande région de Montréal. Avec une équipe de déménageurs expérimentés, et un accent sur le service à la clientèle. Déménagement Vellour cherche à offrir une expérience de première classe à tous ses clients.

Target Market(s)

people selling or buying homes
people going to the bank for a load or real estate

company discounts

Requirements
Must have
• inviting
suprise e
Nice to have
• packages
why vellour

we offer storage solution bundles for products online reservation many methodes of payment

must also be french first then english and chinees mandarin
Should not have
• dates on promotion
prices

```html
<!DOCTYPE html>
<html lang="fr">
<head>
<meta charset="utf-8">
<title>Déménagement Vellour — Flyer</title>
<link href="https://fonts.googleapis.com/css2?family=Montserrat:wght@300;400;500;600;700;800&family=Noto+Sans+SC:wght@400;700&display=swap" rel="stylesheet">
<style>
  :root{
    --navy:#1f3a66;
    --grey-panel:#ebebeb;
    --grey-line:#c4c4c4;
    --grey-button:#d2d2d2;
    --ink:#2b2b2b;
    --text:#4a4a4a;
    --white:#ffffff;
    --page:#f1f1f1;
    --soft-white:#dfe6f1;
  }
  *{margin:0;padding:0;box-sizing:border-box;}
  html,body{width:783px;height:1200px;overflow:hidden;background:var(--page);font-family:"Montserrat",sans-serif;}
  .zh{font-family:"Noto Sans SC","Montserrat",sans-serif;}
  .flyer{position:absolute;left:32px;top:91px;width:719px;height:1018px;background:var(--white);overflow:hidden;box-shadow:0 2px 10px rgba(0,0,0,.12);}
  .hero-art{position:absolute;left:0;top:0;width:719px;height:500px;}

  .brand{position:absolute;left:43px;top:62px;display:flex;align-items:center;gap:12px;}
  .brand-dot{width:46px;height:46px;border:4px solid var(--navy);border-radius:50%;}
  .brand-name{font-weight:800;font-size:34px;color:var(--navy);letter-spacing:1px;line-height:1;}
  .brand-sub{font-weight:700;font-size:9.5px;color:var(--navy);letter-spacing:.3px;margin-top:5px;}

  .hero-copy{position:absolute;left:46px;top:200px;width:250px;color:var(--white);}
  .hero-title{font-weight:700;line-height:1.1;}
  .hero-title .lead{display:block;font-size:33px;letter-spacing:.3px;}
  .hero-title .rest{display:block;font-size:21.5px;letter-spacing:0;}
  .hero-rule{width:58px;height:2px;background:var(--white);margin:12px 0 13px;}
  .hero-tagline{font-weight:700;font-size:12px;line-height:1.35;}
  .hero-tagline-alt{font-weight:500;font-size:10.5px;line-height:1.4;color:var(--soft-white);margin-top:6px;}
  .hero-tagline-alt .zh{font-weight:400;display:block;}
  .hero-button{display:inline-block;margin-top:13px;background:var(--grey-button);color:var(--ink);font-weight:700;font-size:12px;padding:6px 12px;border-radius:10px;letter-spacing:.2px;}

  .services-title{position:absolute;top:484px;left:0;width:719px;display:flex;justify-content:center;align-items:center;gap:8px;font-size:22px;color:var(--ink);font-weight:400;}
  .services-title b{font-weight:700;color:var(--navy);}
  .services-title .line{width:126px;height:1.5px;background:var(--navy);}

  .services-panel{position:absolute;left:0;top:570px;width:719px;height:180px;background:var(--grey-panel);display:flex;}
  .service{flex:1;position:relative;text-align:center;}
  .service + .service{border-left:3px solid var(--white);}
  .service-badge{position:absolute;left:50%;top:-40px;transform:translateX(-50%);width:86px;height:86px;border-radius:50%;background:var(--white);border:1.5px solid var(--navy);display:flex;align-items:center;justify-content:center;}
  .service-badge .ring{width:74px;height:74px;border-radius:50%;border:6px solid var(--navy);display:flex;align-items:center;justify-content:center;background:var(--white);}
  .service-name{position:absolute;top:60px;left:0;right:0;font-weight:700;font-size:11.5px;color:var(--ink);line-height:1.25;}
  .service-desc{position:absolute;top:98px;left:50%;transform:translateX(-50%);width:176px;font-size:10.5px;color:var(--text);line-height:1.25;}

  .promo{position:absolute;left:0;top:750px;width:719px;height:198px;}
  .promo-visual{position:absolute;left:60px;top:26px;width:230px;height:144px;background:linear-gradient(180deg,#5c7ea0 0%,#8aa5bd 45%,#4a5566 70%,#2a2f3a 100%);border:3px solid #1b1b1b;}
  .promo-copy{position:absolute;left:326px;top:40px;width:335px;}
  .promo-title{font-weight:700;font-size:13.3px;line-height:1.3;color:var(--navy);}
  .promo-title .dark{color:var(--ink);}
  .promo-rule{width:24px;height:2px;background:var(--navy);margin:10px 0 12px;}
  .promo-text{font-size:10.3px;color:var(--text);line-height:1.3;}

  .footer{position:absolute;left:0;top:948px;width:719px;height:70px;}
  .footer svg{position:absolute;left:0;top:0;}
  .footer-call{position:absolute;left:40px;top:22px;color:var(--white);font-size:19px;font-weight:300;letter-spacing:.5px;}
  .footer-call strong{font-weight:700;font-size:21px;margin-left:6px;letter-spacing:.5px;}
  .footer-web{position:absolute;left:455px;top:19px;font-weight:700;font-size:12.5px;color:var(--ink);}
</style>
</head>
<body>
<main class="flyer">

  <svg class="hero-art" viewBox="0 0 719 500">
    <defs>
      <linearGradient id="heroPhotoTone" x1="0" y1="0" x2="1" y2="1">
        <stop offset="0" stop-color="#e9eef3"/>
        <stop offset="0.45" stop-color="#c9b08f"/>
        <stop offset="0.7" stop-color="#2f4f86"/>
        <stop offset="1" stop-color="#d9d9d9"/>
      </linearGradient>
    </defs>
    <path fill="var(--navy)" d="M0,148 L285,148 Q312,148 326,122 L345,90 Q360,72 392,72 L719,72 L719,495 Q719,462 690,462 L0,462 Z"/>
    <path fill="var(--grey-line)" d="M0,454 L700,454 Q719,456 719,478 L719,500 Q719,470 690,468 L0,468 Z"/>
    <path fill="var(--grey-line)" d="M405,34 L719,34 L719,438 L396,438 Q360,436 342,404 L296,262 Q290,240 302,218 L368,72 Q382,36 405,34 Z"/>
    <path fill="url(#heroPhotoTone)" role="img" aria-label="Photo de deux déménageurs chargeant des boîtes dans une camionnette" d="M420,38 L719,38 L719,430 L402,430 Q372,428 356,398 L310,262 Q303,242 313,222 L382,76 Q396,40 420,38 Z"/>
  </svg>

  <header class="brand">
    <span class="brand-dot"></span>
    <div>
      <div class="brand-name">VELLOUR</div>
      <div class="brand-sub">DÉMÉNAGEMENT &amp; TRANSPORT</div>
    </div>
  </header>

  <section class="hero-copy">
    <h1 class="hero-title">
      <span class="lead">COMMENCEZ</span>
      <span class="rest">VOTRE PROCHAIN</span>
      <span class="rest">DÉMÉNAGEMENT ICI</span>
    </h1>
    <div class="hero-rule"></div>
    <p class="hero-tagline">Le déménagement peut être stressant.<br>Nous pouvons aider.</p>
    <p class="hero-tagline-alt">Moving can be stressful. We can help.<span class="zh" lang="zh-Hans">搬家很辛苦，我们可以帮您。</span></p>
    <span class="hero-button">RÉSERVER MAINTENANT</span>
  </section>

  <h2 class="services-title"><span class="line"></span>OUR <b>SERVICES</b><span class="line"></span></h2>

  <section class="services-panel">
    <article class="service">
      <div class="service-badge"><div class="ring">
        <svg width="30" height="30" viewBox="0 0 30 30" fill="none" stroke="#8a8a8a" stroke-width="1.6"><path d="M4,15 L15,5 L26,15"/><path d="M7,13 V26 H23 V13"/><rect x="12" y="18" width="6" height="8"/></svg>
      </div></div>
      <h3 class="service-name">DÉMÉNAGEMENT<br>RÉSIDENTIEL</h3>
      <p class="service-desc">Déménager dans votre nouvelle maison ne pourrait pas être plus facile. Notre équipe est prête à vous aider.</p>
    </article>
    <article class="service">
      <div class="service-badge"><div class="ring">
        <svg width="30" height="30" viewBox="0 0 30 30" fill="none" stroke="#8a8a8a" stroke-width="1.6"><rect x="9" y="4" width="12" height="22"/><rect x="4" y="14" width="5" height="12"/><rect x="21" y="11" width="5" height="15"/><path d="M12,8 H18 M12,12 H18 M12,16 H18 M2,26 H28"/></svg>
      </div></div>
      <h3 class="service-name">TRANSPORT<br>COMMERCIAL</h3>
      <p class="service-desc">A votre service pour tous vos transport commerciaux. Service rapide, efficace et digne de confiance!</p>
    </article>
    <article class="service">
      <div class="service-badge"><div class="ring">
        <svg width="32" height="32" viewBox="0 0 32 32" fill="none" stroke="#8a8a8a" stroke-width="1.6"><path d="M16,4 L28,10 L16,16 L4,10 Z"/><path d="M4,10 V22 L16,28 L28,22 V10"/><path d="M16,16 V28"/></svg>
      </div></div>
      <h3 class="service-name">FOURNITURES DE<br>DÉMÉNAGEMENT</h3>
      <p class="service-desc">Toutes les fournitures dont vous aurez besoin pour compléter votre déménagement.</p>
    </article>
  </section>

  <section class="promo">
    <div class="promo-visual" role="img" aria-label="Téléviseur grand écran offert en promotion"></div>
    <div class="promo-copy">
      <h3 class="promo-title"><span class="dark">PROMOTION: GAGNANTE TV PROMO</span><br>PROMOTION DÉMÉNAGEMENT - TIRAGE</h3>
      <div class="promo-rule"></div>
      <p class="promo-text">Bravo a Camille Dufresne de Laval !!!! je suis certain que vous et la famille sera bien vous servir de cette Magnifique TV ORVANTA ! encore Félicitation ! Déménagement Vellour Promotions et Rabais</p>
    </div>
  </section>

  <footer class="footer">
    <svg width="719" height="70" viewBox="0 0 719 70" aria-hidden="true">
      <rect width="719" height="70" fill="var(--navy)"/>
      <path fill="var(--white)" d="M395,0 L719,0 L719,59 L470,59 Q448,59 436,40 Q420,10 395,0 Z"/>
      <path fill="var(--grey-line)" d="M410,0 L719,0 L719,56 L478,56 Q458,56 447,38 Q432,8 410,0 Z"/>
    </svg>
    <p class="footer-call">CALL US NOW: <strong>514.555.0142</strong></p>
    <p class="footer-web">www.demenagementvellour.com</p>
  </footer>

</main>
</body>
</html>
```